Webseite Toilettenvermietung
Zielgruppe
Wir vermieten mobile Toilettenkabine und Toilettenwagen. Wir haben noch eine Webseite kabinenpark-nord.de und lokus-verleihhaus.de und benötigen noch eine weitere. Es sollen nur die Miettoiletten und Toilettenwagen beworben werden
Aufgabenstellung
saubere und aussageräftige, farbliches Erscheinungsbild der Startseite.

```html
<!DOCTYPE html>
<html lang="de">
<head>
<meta charset="utf-8">
<title>KLARO – Mobile Raum- &amp; Sanitärsysteme</title>
<link href="https://fonts.googleapis.com/css2?family=Source+Sans+3:wght@400;600;700;800&family=Arimo:wght@400;700&family=PT+Sans+Narrow&display=swap" rel="stylesheet">
<style>
  :root{
    --brand:#0a5fae;
    --brand-dark:#064b8c;
    --ink:#111;
    --card:#dbe7f3;
    --nav:#000;
    --white:#fff;
    --grey:#9a9a9a;
  }
  *{margin:0;padding:0;box-sizing:border-box}
  html,body{width:823px;height:1200px;overflow:hidden;background:var(--white)}
  body{position:relative;font-family:"Source Sans 3",sans-serif;color:var(--ink)}
  .brand{position:absolute;left:38px;top:22px;display:flex;align-items:center;gap:8px}
  .brand-mark{width:30px;height:30px;border-radius:50%;background:var(--brand)}
  .brand-text{color:var(--brand);font-weight:800;line-height:1}
  .brand-name{font-size:30px;letter-spacing:1px}
  .brand-tag{font-size:10px;margin-top:3px}
  .meta{position:absolute;right:41px;top:29px;font-family:"Arimo",sans-serif;font-size:10px;color:#222}
  .meta-links{display:flex;gap:15px;justify-content:flex-end;font-weight:700;letter-spacing:.3px}
  .meta-contact{display:flex;gap:18px;margin-top:5px;font-weight:700;font-size:10.5px}
  .meta-contact span{display:flex;align-items:center;gap:6px}
  .main-nav{position:absolute;left:32px;top:95px;width:759px;height:63px;background:var(--nav);display:flex;align-items:center}
  .main-nav a{color:var(--white);text-decoration:none;font-size:17.5px;padding:0 10px;height:100%;display:flex;align-items:center}
  .main-nav a.active{background:var(--brand);padding:0 11px}
  .hero{position:absolute;left:32px;top:181px;width:759px;height:310px;background:linear-gradient(180deg,#0b1f6b 0%,#1b3a8a 50%,#2a3a4a 72%,#10161c 100%)}
  .intro{position:absolute;right:32px;top:508px;width:720px;text-align:right;font-size:12px;line-height:16px}
  .intro h2{font-weight:400;font-size:15px;margin-bottom:4px}
  .intro em{font-style:normal;font-size:14.5px}
  .card{position:absolute;top:581px;height:325px;background:var(--card);box-shadow:2px 4px 6px rgba(0,0,0,.35);padding:14px 9px}
  .card h3{font-weight:400;font-size:17px;line-height:22px;text-transform:uppercase}
  .card p{font-size:10.2px;line-height:13.6px;margin-top:10px}
  .card .product{position:absolute;border-radius:3px}
  .card .btn{position:absolute;bottom:11px;height:34px;width:82px;background:var(--brand);color:var(--white);font-family:"Arimo",sans-serif;font-weight:700;text-align:center;display:flex;flex-direction:column;justify-content:center;line-height:1.05}
  .btn-info{left:10px}
  .btn-info small{font-size:10.5px}
  .btn-info b{font-size:14px}
  .btn-request{right:10px;font-size:11.5px}
  .districts-title{position:absolute;right:32px;top:925px;font-size:12px}
  .district{position:absolute;top:950px;width:134px;height:172px;background:var(--brand);color:var(--white);text-align:right;padding:8px 8px 0 0;font-size:12.3px;line-height:15.85px;box-shadow:2px 4px 6px rgba(0,0,0,.35);list-style:none}
  .footer{position:absolute;left:0;width:823px;top:1141px;text-align:center;font-family:"PT Sans Narrow",sans-serif;color:var(--brand);font-size:14px;line-height:19px}
  .corner{position:absolute;left:0;top:1178px;width:22px;height:22px;background:var(--grey)}
</style>
</head>
<body>
  <header>
    <div class="brand">
      <div class="brand-mark"></div>
      <div class="brand-text">
        <div class="brand-name">KLARO</div>
        <div class="brand-tag">Mobile Raum- &amp; Sanitärsysteme</div>
      </div>
    </div>
    <div class="meta">
      <nav class="meta-links"><span>BESTELLUNG</span><span>KONTAKT</span><span>AGB</span><span>IMPRESSUM</span></nav>
      <div class="meta-contact">
        <span><svg width="14" height="11" viewBox="0 0 14 11"><path d="M1 4c0-2 2-3 6-3s6 1 6 3v1h-3V3.5H4V5H1z" fill="#555"/><rect x="2.5" y="5.5" width="9" height="5" rx="1" fill="#555"/></svg>+ 49 2100 48 27 - 30</span>
        <span><svg width="14" height="10" viewBox="0 0 14 10"><rect width="14" height="10" fill="#555"/><path d="M0 0l7 5 7-5" stroke="#fff" fill="none"/></svg>info@klaro-miete.de</span>
      </div>
    </div>
  </header>

  <nav class="main-nav">
    <a class="active">HOME</a><a>TOILETTENKABINE</a><a>TOILETTENWAGEN</a><a>ANFRAGEN</a>
  </nav>

  <div class="hero" role="img" aria-label="Nachtaufnahme einer Kirmes mit beleuchtetem Riesenrad, Achterbahn und Fahrgeschäften"></div>

  <section class="intro">
    <h2>Lorem ipsum</h2>
    <p>Lorem ipsum dolor sit amet, consetetur sadipscing elitr, sed diam nonumy eirmod <em>Lorem ipsum</em> Lorem ipsum dolor sit amet,<br>consetetusadipscing elitr, sed diam nonumy eirmod tempor invidunt ut labore et dolore magna aliquyam erat, sed diam voluptua.</p>
  </section>

  <article class="card" style="left:32px;width:240px">
    <h3>Mobile WC Kabinen<br>mieten</h3>
    <p>Unsere WC-Kabinen zum mieten bzw im Verleih. Hier finden Sie unsere Toilettenkabinen wie z. B. das mobile Baustellen WC, unser Universal Miete WC oder den Urinalstand in der Übersicht.</p>
    <div class="product" role="img" aria-label="Türkisfarbene mobile Toilettenkabine" style="left:84px;top:133px;width:80px;height:135px;background:linear-gradient(90deg,#1a9c8f,#2bb8a8)"></div>
    <div class="btn btn-info"><small>weitere</small><b>INFOS</b></div>
    <div class="btn btn-request">ANFRAGEN</div>
  </article>

  <article class="card" style="left:294px;width:231px">
    <h3>Rollstuhl WC Kabinen<br>mieten</h3>
    <p>Die praktische Rollstuhlgerechte WC Kabine zu mieten hier bei KLARO - WC Mietservice.</p>
    <div class="product" role="img" aria-label="Geöffnete rollstuhlgerechte WC-Kabine in Grün" style="left:60px;top:114px;width:120px;height:148px;background:linear-gradient(90deg,#1e7a6a,#3a8a7e 45%,#e8ecee 55%,#d6dadd)"></div>
    <div class="btn btn-info"><small>weitere</small><b>INFOS</b></div>
    <div class="btn btn-request">ANFRAGEN</div>
  </article>

  <article class="card" style="left:547px;width:244px">
    <h3>Mobile WC Wagen<br>mieten</h3>
    <p>Hier finden Sie unsere WC Wagen in der Übersicht zur Vermietung, zum Verleih. Vom normalen Toilettenwagen (1x Dame / 1x Herren) bis hin zum exklusiven WC Wagen / Toilettenwagen.</p>
    <div class="product" role="img" aria-label="Weißer Toilettenwagen mit geöffneten Türen und Treppen" style="left:8px;top:165px;width:228px;height:96px;background:linear-gradient(180deg,#f4f5f7 0%,#e6e8ec 72%,#2a2f8a 78%,#1f2570 100%)"></div>
    <div class="btn btn-info"><small>weitere</small><b>INFOS</b></div>
    <div class="btn btn-request">ANFRAGEN</div>
  </article>

  <div class="districts-title">Stadtteile Düsseldorf</div>
  <ul class="district" style="left:32px"><li>Altstadt</li><li>Angermund</li><li>Benrath</li><li>Bilk</li><li>Carlstadt</li><li>Derendorf</li><li>Düsseltal</li><li>Eller</li><li>Flehe</li><li>Flingern Nord</li></ul>
  <ul class="district" style="left:188px"><li>Flingern Süd</li><li>Friedrichstadt</li><li>Garath</li><li>Gerresheim</li><li>Golzheim</li><li>Grafenberg</li><li>Hafen</li><li>Hamm</li><li>Hassels</li><li>Heerdt</li></ul>
  <ul class="district" style="left:344px"><li>Hellerhof</li><li>Himmelgeist</li><li>Holthausen</li><li>Hubbelrath</li><li>Itter</li><li>Kaiserswerth</li><li>Kalkum</li><li>Lörick</li><li>Lichtenbroich</li><li>Lierenfeld</li></ul>
  <ul class="district" style="left:500px"><li>Lohausen</li><li>Ludenberg</li><li>Mörsenbroich</li><li>Niederkassel</li><li>Oberbilk</li><li>Oberkassel</li><li>Pempelfort</li><li>Rath</li><li>Reisholz</li><li>Stadtmitte</li></ul>
  <ul class="district" style="left:656px"><li>Stockum</li><li>Unterbach</li><li>Unterbilk</li><li>Unterrath</li><li>Urdenbach</li><li>Vennhausen</li><li>Volmerswerth</li><li>Wersten</li><li>Wittlaer</li></ul>

  <footer class="footer">© 2014 Klaro.<br>All Rights Reserved.</footer>
  <div class="corner"></div>
</body>
</html>
```